Yard Sign Design for luxury design & build company

Looking to have 18" x 24" company yard signs designed.
An update to the business logo might be helpful.
Photos are not necessary but use if you can make inspiring.

Industry: Construction

Looking for a large headline of "Basement Finishing"
Website: www.tamberlyhomes.com
Phone Number (612) 555-0174
FB link: facebook.com/tamberlyhomesmn
Instagram: www.instagram.com/tamberlyhomesmn

Industry/Entity Type

Construction

Colors

Designer to choose colors to be used in the design.

Requirements
Must have
• Impactful high end characteristics
Nice to have
• Depth and detail graphis

```html
<!DOCTYPE html>
<html lang="en">
<head>
<meta charset="utf-8">
<title>Tamberly Homes – Basement Finishing Yard Sign</title>
<link rel="stylesheet" href="https://fonts.googleapis.com/css2?family=Bebas+Neue&family=Poppins:wght@600;700;800&display=swap">
<style>
  :root {
    --page-bg: #e4e4e4;
    --sign-white: #ffffff;
    --band-black: #111111;
    --band-charcoal: #2b2b2b;
    --brand-red: #d8262a;
    --ink: #111111;
    --frame-steel: #5a6070;
    --photo-warm: #8a6a4c;
    --photo-light: #d9d4cc;
    --photo-shadow: #4a3f36;
    --badge-grey: #ececec;
  }
  * { margin: 0; padding: 0; box-sizing: border-box; }
  html, body {
    width: 1200px;
    height: 2400px;
    overflow: hidden;
    background: var(--page-bg);
  }
  .yard-sign {
    position: absolute;
    left: 50px;
    top: 788px;
    width: 1100px;
    height: 825px;
    background: var(--sign-white);
    box-shadow: 0 6px 18px rgba(0,0,0,0.25);
    overflow: hidden;
  }
  .hero-band {
    position: absolute;
    left: 0; top: 0;
    width: 1100px;
    height: 445px;
    background: linear-gradient(100deg, var(--band-black) 0%, var(--band-charcoal) 45%, var(--band-black) 100%);
  }
  .headline {
    position: absolute;
    left: 78px;
    font-family: "Bebas Neue", "Oswald", sans-serif;
    line-height: 1;
    white-space: nowrap;
  }
  .headline-top {
    top: 92px;
    font-size: 160px;
    color: var(--sign-white);
    letter-spacing: -1px;
  }
  .headline-bottom {
    top: 212px;
    font-size: 174px;
    color: var(--brand-red);
    letter-spacing: -2px;
  }
  .photo-frame {
    position: absolute;
    left: 625px; top: 27px;
    width: 455px; height: 330px;
    border: 3px solid var(--frame-steel);
  }
  .project-photo {
    position: absolute;
    left: 600px; top: 68px;
    width: 452px; height: 316px;
    background: linear-gradient(170deg, var(--photo-light) 0%, #b9b2a6 35%, var(--photo-warm) 70%, var(--photo-shadow) 100%);
    border: 2px solid #ddd;
  }
  .phone-bar {
    position: absolute;
    left: 76px; top: 412px;
    width: 947px; height: 125px;
    background: var(--brand-red);
    border-radius: 20px;
    display: flex;
    align-items: center;
    padding-left: 34px;
  }
  .phone-icon {
    width: 74px; height: 74px;
    flex: none;
  }
  .phone-number {
    margin-left: 18px;
    font-family: "Poppins", sans-serif;
    font-weight: 800;
    font-size: 108px;
    line-height: 1;
    color: var(--sign-white);
    letter-spacing: -1px;
    white-space: nowrap;
    padding-top: 10px;
  }
  .website {
    position: absolute;
    left: 76px; top: 548px;
    width: 947px;
    text-align: center;
    font-family: "Poppins", sans-serif;
    font-weight: 700;
    font-size: 62px;
    letter-spacing: 6px;
    color: var(--ink);
    white-space: nowrap;
  }
  .brand-mark {
    position: absolute;
    left: 64px; top: 645px;
    width: 108px; height: 108px;
    border-radius: 50%;
    border: 4px solid var(--ink);
  }
  .brand-name {
    position: absolute;
    left: 186px; top: 664px;
    font-family: "Poppins", sans-serif;
    font-weight: 700;
    font-size: 34px;
    line-height: 1.1;
    letter-spacing: 3px;
    color: var(--ink);
  }
  .review-badge {
    position: absolute;
    left: 412px; top: 655px;
    width: 235px; height: 90px;
    border-radius: 12px;
    background: var(--badge-grey);
  }
  .social-dot {
    position: absolute;
    left: 687px; top: 648px;
    width: 50px; height: 50px;
    border-radius: 50%;
    background: var(--ink);
  }
  .social-handle {
    position: absolute;
    left: 687px; top: 706px;
    font-family: "Bebas Neue", "Oswald", sans-serif;
    font-size: 56px;
    line-height: 1;
    color: var(--ink);
    white-space: nowrap;
  }
</style>
</head>
<body>
  <main class="yard-sign">
    <div class="hero-band" role="img" aria-label="Dark, faded photo of a finished basement interior"></div>
    <div class="headline headline-top">BASEMENT</div>
    <div class="headline headline-bottom">FINISHING</div>
    <div class="photo-frame"></div>
    <div class="project-photo" role="img" aria-label="Photo of a finished basement with sectional sofa, wood floor, bar and fireplace"></div>

    <div class="phone-bar">
      <svg class="phone-icon" viewBox="0 0 74 74" aria-hidden="true">
        <circle cx="37" cy="37" r="37" fill="#111"/>
        <path d="M27 19c2 0 3 1 4 3l3 7c1 2 0 3-1 4l-3 3c2 5 6 9 11 11l3-3c1-1 2-2 4-1l7 3c2 1 3 2 3 4v4c0 3-2 5-5 5-17 0-30-13-30-30 0-3 2-5 5-5z" fill="#fff"/>
      </svg>
      <span class="phone-number">(612) 555-0174</span>
    </div>

    <div class="website">www.tamberlyhomes.com</div>

    <div class="brand-mark"></div>
    <div class="brand-name">TAMBERLY<br>HOMES</div>

    <div class="review-badge"></div>

    <div class="social-dot"></div>
    <div class="social-handle">@TAMBERLYHOMESMN</div>
  </main>
</body>
</html>
```